Business Card Design Project

I need a business card design for a new business called Tolland Insurance Services. I am a small insurance broker that will provide business insurance services mostly to contractors and small businesses. My business is all about customer service and assistance rather than being a price driven/focused business. I want my business card to be professional giving the impression that I am larger than one person but not a corporate company. I have attached a copy of my logo.
Updates

Hi all

I have been advised that I need to show the following info for compliance reasons on my card. It only has to be small.

Can you please include either front or back:

Tolland Insurance Services Pty Ltd [ABN 61827405193] AR No 586714 as Authorised Representative of Brackford Insurance Group Pty Ltd ACN 274 906 518 ABN 82 274 906 518 AFS Licence No 718264

Reason: I need a further change to be made to the design. I need the contact number of 1300476815 added to the business card.

Hi All

I need one last change made to the card.

Can you please include the phone number 1300476815 to the card. If possible can this be made fairly clear on the card, either large on the back or another design idea you may have.

Target Market(s)

30+ Professionals

Industry/Entity Type

Insurance

Requirements
Must have
• I want a double sided design. My details to go on the card are as follows:

Dylan Tolland QRPSUV (Snr Assoc.) CIP
Director
PO Box 872, Kestrelvale SA 5091
Phone: 0438 617 204
Fax 08 8397 2418
Email: dylan@tollandinsure.example
Website: http://www.tollandinsure.example
Twitter: Tollandinsure
Facebook: facebook.com/tollandinsure

```html
<!DOCTYPE html>
<html lang="en">
<head>
<meta charset="utf-8">
<title>Tolland Insurance – Business Card</title>
<link href="https://fonts.googleapis.com/css2?family=Arimo:ital,wght@0,400;0,700;1,400&family=Questrial&display=swap" rel="stylesheet">
<style>
  :root {
    --bg: #e4e4e4;
    --red: #d4161c;
    --red-dark: #a50e12;
    --white: #ffffff;
    --ink: #1e1e1e;
    --grey: #555555;
    --silver-light: #f2f2f2;
    --silver-dark: #b9b9b9;
  }
  * { margin: 0; padding: 0; box-sizing: border-box; }
  html, body { width: 1200px; height: 944px; overflow: hidden; background: var(--bg); }
  body { position: relative; font-family: "Arimo", Arial, sans-serif; }

  .card {
    position: absolute;
    left: 220px;
    width: 760px;
    height: 434px;
    overflow: hidden;
    box-shadow: 0 6px 18px rgba(0,0,0,0.25);
  }
  .card-front { top: 24px; background: var(--white); }
  .card-back { top: 486px; background: var(--red); }

  .card-shape { position: absolute; inset: 0; width: 100%; height: 100%; }

  /* front */
  .brand {
    position: absolute;
    left: 150px;
    top: 96px;
    display: flex;
    align-items: center;
    gap: 16px;
  }
  .brand-dot { width: 30px; height: 30px; border-radius: 50%; background: var(--red); flex: none; }
  .brand-name {
    font-family: "Questrial", Arial, sans-serif;
    font-size: 50px;
    color: var(--ink);
    letter-spacing: 0.5px;
  }
  .tagline {
    position: absolute;
    left: 196px;
    top: 164px;
    width: 380px;
    font-size: 13px;
    letter-spacing: 3px;
    color: var(--grey);
    text-align: center;
    border-top: 1px solid #999;
    border-bottom: 1px solid #999;
    padding: 3px 0;
  }
  .compliance {
    position: absolute;
    left: 120px;
    right: 100px;
    top: 262px;
    font-size: 15px;
    line-height: 1.35;
    color: var(--ink);
    text-align: center;
  }

  /* back */
  .details {
    position: absolute;
    left: 58px;
    top: 48px;
    color: var(--white);
    font-size: 19px;
    line-height: 1.25;
  }
  .person-name { font-size: 24px; }
  .person-role { font-style: italic; font-size: 17px; }
  .credentials { font-size: 16px; margin-bottom: 36px; }
  .postal { margin-bottom: 30px; }
  .back-brand {
    position: absolute;
    left: 530px;
    top: 140px;
    width: 200px;
    text-align: center;
  }
  .back-brand .brand-dot { width: 34px; height: 34px; margin: 0 auto 14px; }
  .back-brand-name {
    font-family: "Questrial", Arial, sans-serif;
    font-size: 42px;
    color: var(--ink);
  }
  .hotline {
    position: absolute;
    left: 510px;
    top: 300px;
    width: 240px;
    text-align: center;
    font-weight: 700;
    font-size: 28px;
    color: var(--red);
    letter-spacing: 1px;
  }
</style>
</head>
<body>

<section class="card card-front" aria-label="Card front">
  <svg class="card-shape" viewBox="0 0 760 434" preserveAspectRatio="none" aria-hidden="true">
    <defs>
      <linearGradient id="redSide" x1="0" x2="1">
        <stop offset="0" stop-color="#a50e12"/>
        <stop offset="1" stop-color="#d4161c"/>
      </linearGradient>
    </defs>
    <path d="M0 0 H70 Q30 217 70 434 H0 Z" fill="url(#redSide)"/>
    <path d="M760 0 H700 Q740 217 700 434 H760 Z" fill="url(#redSide)"/>
    <path d="M70 434 Q380 360 700 434 Z" fill="#dcdcdc"/>
  </svg>
  <div class="brand">
    <span class="brand-dot"></span>
    <span class="brand-name">tolland insurance</span>
  </div>
  <p class="tagline">insurance advice you can trust</p>
  <p class="compliance">Tolland Insurance Services Pty Ltd [ABN 61827405193] AR No 586714 as Authorised Representative of Brackford Insurance Group Pty Ltd ACN 274 906 518 ABN 82 274 906 518 AFS Licence No 718264</p>
</section>

<section class="card card-back" aria-label="Card back">
  <svg class="card-shape" viewBox="0 0 760 434" preserveAspectRatio="none" aria-hidden="true">
    <defs>
      <linearGradient id="silver" x1="0" y1="0" x2="1" y2="1">
        <stop offset="0" stop-color="#f2f2f2"/>
        <stop offset="0.5" stop-color="#d6d6d6"/>
        <stop offset="1" stop-color="#b9b9b9"/>
      </linearGradient>
    </defs>
    <path d="M480 0 Q520 217 480 434 H760 V0 Z" fill="url(#silver)"/>
  </svg>
  <div class="details">
    <p><span class="person-name">Dylan Tolland</span> <span class="person-role">Director</span></p>
    <p class="credentials">QRPSUV (Snr Assoc.) CIP</p>
    <p>PO Box 872, Kestrelvale SA 5091</p>
    <p>Phone: 0438 617 204</p>
    <p class="postal">Fax: 08 8397 2418</p>
    <p>E: dylan@tollandinsure.example</p>
    <p>www.tollandinsure.example</p>
    <p>Twitter: Tollandinsure</p>
    <p>facebook.com/tollandinsure</p>
  </div>
  <div class="back-brand">
    <div class="brand-dot"></div>
    <p class="back-brand-name">tolland</p>
  </div>
  <p class="hotline">1300476815</p>
</section>

</body>
</html>
```